Purchase Protection Subscription Program needs a refreshed website

We are refreshing an existing website www.buyguardian720.com. This is a purchase protection product which allows its members to receive extended warranty on the items they buy, receive a rebate of 50% on a repair of an item, a personal shopping concierge, etc. We are looking for a fresh, clean approach - with mass appeal to both men and woman. The site should convey trust, and ease of use.
Updates

Thanks to everyone who posted designs. Amazing work! It was a very difficult decision!

Industry/Entity Type

Product

```html
<!DOCTYPE html>
<html lang="en">
<head>
<meta charset="utf-8">
<title>BuyGuardian 720 – Purchase Protection</title>
<link href="https://fonts.googleapis.com/css2?family=Open+Sans:wght@300;400;600;700&display=swap" rel="stylesheet">
<style>
  :root {
    --ink: #111111;
    --muted: #9aa1a8;
    --line: #e4e6e8;
    --white: #ffffff;
    --footer-bg: #222222;
    --footer-text: #8c8c8c;
    --footer-head: #f0f0f0;
    --field: #3a3a3a;
  }
  * { box-sizing: border-box; margin: 0; padding: 0; }
  html, body { width: 1147px; height: 1200px; overflow: hidden; background: var(--white); }
  body { font-family: "Open Sans", Arial, sans-serif; color: var(--ink); position: relative; }
  a { color: inherit; text-decoration: none; }

  .utility { position: absolute; top: 7px; right: 153px; display: flex; gap: 20px; font-size: 9.5px; color: #8a8a8a; }
  .utility a::before { content: ""; display: inline-block; width: 4px; height: 4px; background: #aaa; margin-right: 8px; vertical-align: middle; }

  .brand { position: absolute; left: 154px; top: 40px; font-size: 19px; font-weight: 400; letter-spacing: -0.3px; color: var(--ink); }

  .main-nav { position: absolute; right: 153px; top: 49px; display: flex; gap: 21px; font-size: 10.4px; font-weight: 400; text-transform: uppercase; letter-spacing: 0.1px; }

  .hero { position: absolute; left: 155px; top: 107px; width: 839px; height: 341px; overflow: hidden;
    background: linear-gradient(100deg, #b9a3a9 0%, #8a7f7c 22%, #5a4a40 38%, #c7b9ad 55%, #d8d2cc 70%, #cfc8c4 100%); }
  .hero-photo { position: absolute; inset: 0; }
  .hero-title { position: absolute; left: 453px; top: 82px; color: var(--white); font-weight: 700; font-size: 33px; letter-spacing: 0.2px; text-shadow: 0 1px 3px rgba(0,0,0,0.25); }
  .hero-sub { position: absolute; left: 453px; top: 126px; color: var(--white); font-weight: 700; font-size: 17.5px; text-shadow: 0 1px 3px rgba(0,0,0,0.25); }
  .hero-sub .tag { background: #0a0a0a; padding: 0 4px; text-shadow: none; }
  .hero-arrow { position: absolute; top: 158px; width: 26px; height: 26px; }
  .hero-arrow.prev { left: 28px; }
  .hero-arrow.next { right: 28px; }
  .hero-dots { position: absolute; left: 391px; top: 318px; display: flex; gap: 9px; }
  .hero-dots span { width: 12px; height: 12px; border-radius: 50%; border: 1.5px solid var(--white); position: relative; }
  .hero-dots span.active::after { content: ""; position: absolute; left: 2.5px; top: 2.5px; width: 4px; height: 4px; border-radius: 50%; background: var(--white); }

  .features { position: absolute; top: 534px; left: 0; width: 1147px; }
  .feature { position: absolute; width: 290px; text-align: center; }
  .feature:nth-child(1) { left: 142px; }
  .feature:nth-child(2) { left: 428px; }
  .feature:nth-child(3) { left: 715px; }
  .feature-icon { display: block; margin: 0 auto; width: 92px; height: 92px; }
  .feature h2 { font-size: 13.6px; font-weight: 600; margin-top: 18px; }
  .feature p { font-size: 10.2px; line-height: 17.2px; color: var(--muted); margin-top: 12px; }
  .feature .dark { color: var(--ink); }
  .feature .plus { font-size: 13px; color: var(--ink); margin-top: 10px; line-height: 18px; }
  .feature .plus + p { margin-top: 0; }
  .btn { position: absolute; top: 233px; left: 50%; transform: translateX(-50%); border: 1px solid var(--ink); font-size: 10.2px; padding: 5px 8px; white-space: nowrap; }

  .disclaimer { position: absolute; top: 840px; left: 154px; width: 840px; }
  .rule-set { position: relative; height: 9px; }
  .rule-set i { position: absolute; height: 1px; background: var(--line); }
  .disclaimer p { font-size: 8.3px; line-height: 17.2px; color: var(--muted); text-align: center; padding: 8px 6px; }

  .site-footer { position: absolute; top: 1007px; left: 0; width: 1147px; height: 193px; background: var(--footer-bg); color: var(--footer-text); }
  .footer-col { position: absolute; top: 33px; }
  .footer-col h3 { font-size: 12px; font-weight: 400; color: var(--footer-head); margin-bottom: 13px; }
  .footer-col p { font-size: 9.4px; line-height: 17.2px; width: 195px; }
  .links { display: grid; grid-template-columns: 89px auto; font-size: 9.1px; line-height: 15px; text-transform: uppercase; }
  .social { display: flex; gap: 15px; margin-top: 12px; }
  .social span { width: 21px; height: 21px; border-radius: 50%; border: 1.3px solid #8c8c8c; }
  .signup { display: flex; gap: 10px; margin-top: 10px; }
  .signup .field { width: 129px; height: 21px; background: var(--field); font-size: 9px; line-height: 21px; padding-left: 7px; color: #777; }
  .signup .ok { width: 24px; height: 21px; background: var(--field); font-size: 9px; line-height: 21px; text-align: center; color: #888; }
  .copyright { position: absolute; left: 154px; top: 170px; font-size: 8.8px; color: #6f6f6f; }
</style>
</head>
<body>
  <nav class="utility"><a href="#">Login</a><a href="#">Manage User Profile</a></nav>
  <div class="brand">BuyGuardian 720</div>
  <nav class="main-nav">
    <a href="#">Home</a><a href="#">About Us</a><a href="#">Privacy</a><a href="#">Product Features</a><a href="#">How It Works</a><a href="#">Contact Us</a>
  </nav>

  <section class="hero">
    <div class="hero-photo" role="img" aria-label="Photo of a smiling shopper holding a pink shopping bag on a blurred street"></div>
    <div class="hero-title">Shop with confidence</div>
    <div class="hero-sub">knowing <span class="tag">BuyGuardian 720</span> is there...</div>
    <svg class="hero-arrow prev" viewBox="0 0 26 26"><circle cx="13" cy="13" r="12" fill="none" stroke="#fff" stroke-width="1.5"/><path d="M14.5 9 L10.5 13 L14.5 17" fill="none" stroke="#fff" stroke-width="1.3"/></svg>
    <svg class="hero-arrow next" viewBox="0 0 26 26"><circle cx="13" cy="13" r="12" fill="none" stroke="#fff" stroke-width="1.5"/><path d="M11.5 9 L15.5 13 L11.5 17" fill="none" stroke="#fff" stroke-width="1.3"/></svg>
    <div class="hero-dots"><span class="active"></span><span></span><span></span></div>
  </section>

  <section class="features">
    <article class="feature">
      <svg class="feature-icon" viewBox="0 0 92 92">
        <circle cx="46" cy="46" r="44.5" fill="none" stroke="#111" stroke-width="2.4"/>
        <path d="M49 30 L62 35 V46 C62 54 56 59 49 62 C42 59 36 54 36 46 V35 Z" fill="none" stroke="#111" stroke-width="2.4"/>
        <text x="49" y="52" font-family="Open Sans, sans-serif" font-size="15" font-weight="700" text-anchor="middle" fill="#111">$</text>
        <rect x="28" y="57" width="12" height="2.6" fill="#111"/><rect x="28" y="53" width="12" height="2.6" fill="#111"/><rect x="30" y="49" width="10" height="2.6" fill="#111"/><rect x="31" y="45" width="7" height="2.6" fill="#111"/>
      </svg>
      <h2>Valuable Purchase Protection</h2>
      <p>Get 5 unique ways to get more out of the things you buy:</p>
      <p class="dark" style="margin-top:6px">Warranty Extension, Repair Bill Rebate<br>Product Return Guarantee, Price Protection<br>Restocking fee reimbursement</p>
      <a class="btn" href="#">Learn More</a>
    </article>
    <article class="feature">
      <svg class="feature-icon" viewBox="0 0 92 92">
        <circle cx="46" cy="46" r="44.5" fill="none" stroke="#111" stroke-width="2.4"/>
        <rect x="33" y="31" width="24" height="30" fill="none" stroke="#111" stroke-width="2.4"/>
        <path d="M37 61 V64 H60 V35 H57" fill="none" stroke="#111" stroke-width="2.4"/>
        <path d="M37 38 H53 M37 43 H53 M37 48 H53 M37 53 H53" stroke="#111" stroke-width="2"/>
      </svg>
      <h2>Easy Claims Process</h2>
      <p>Using <span class="dark">BuyGuardian 720</span> has never been easier. Just send us copies, scans or photos of your receipts -- we'll store them securely online. Then download what you need and submit your claim online.</p>
      <a class="btn" href="#">Learn More</a>
    </article>
    <article class="feature">
      <svg class="feature-icon" viewBox="0 0 92 92">
        <circle cx="46" cy="46" r="44.5" fill="none" stroke="#111" stroke-width="2.4"/>
        <ellipse cx="44" cy="50" rx="15" ry="11" fill="#111"/>
        <rect x="34" y="56" width="5" height="9" fill="#111"/><rect x="48" y="56" width="5" height="9" fill="#111"/>
        <circle cx="47" cy="35" r="5" fill="#111"/>
        <path d="M58 47 L63 46 L63 52 L58 52 Z" fill="#111"/>
        <text x="47" y="38" font-family="Open Sans, sans-serif" font-size="7" font-weight="700" text-anchor="middle" fill="#fff">$</text>
      </svg>
      <h2>One low monthly fee</h2>
      <div class="plus">PLUS</div>
      <p>Get a <span class="dark">$5 bonus</span><br><span class="dark">Rebate</span> each calendar quarter to use on home electronics &amp; appliance purchases!*</p>
      <a class="btn" href="#">Learn More</a>
    </article>
  </section>

  <section class="disclaimer">
    <div class="rule-set"><i style="left:0;top:0;width:100px"></i><i style="left:0;top:8px;width:145px"></i><i style="right:0;top:0;width:100px"></i><i style="right:0;top:8px;width:145px"></i></div>
    <p>*Exclusions and limitations apply. See Terms and Conditions for complete product benefit details. Warranty Extension and Repair Bill Rebate benefits are not available in Maine. Warranty Extension and Repair Bill Rebate benefits are provided by Northgate Product Care Company, except in Arizona, Florida, Oklahoma and Wisconsin, where they are provided by Service Keeper, Incorporated (FL License Number 00000), both of which are located at 400 Lakeview Ave., Springfield, IL 62701, (555) 013-2040. The programs are administered by Harbor Innovation Solutions, Inc., 400 Lakeview Ave., Springfield, IL 62701, (555) 013-2040. Bonus Rebates are limited to one rebate per purchased item and one purchase per calendar quarter.</p>
    <div class="rule-set"><i style="left:0;top:0;width:145px"></i><i style="left:0;top:8px;width:100px"></i><i style="right:0;top:0;width:145px"></i><i style="right:0;top:8px;width:100px"></i></div>
  </section>

  <footer class="site-footer">
    <div class="footer-col" style="left:154px">
      <h3>About BuyGuardian 720</h3>
      <p>Lorem ipsum dolor sit amet, consectetur adipiscing elit. Aenean pharetra elit in nulla commodo, lobortis pretium nulla porta. Curabitur vitae purus ullamcorper, sodales odio eget, ultricies risus.</p>
    </div>
    <div class="footer-col" style="left:368px">
      <h3>Useful Links</h3>
      <div class="links"><a href="#">Home</a><a href="#">Product Features</a><a href="#">About Us</a><a href="#">How It Works</a><a href="#">Privacy</a><a href="#">Contact Us</a></div>
    </div>
    <div class="footer-col" style="left:583px">
      <h3>Find Us:</h3>
      <div class="social"><span></span><span></span><span></span><span></span></div>
    </div>
    <div class="footer-col" style="left:800px">
      <h3>Join Mailing List:</h3>
      <div class="signup"><div class="field">Email Adress...</div><div class="ok">OK</div></div>
    </div>
    <div class="copyright">Copyright © 2014 BuyGuardian 720. All Rights Reserved.</div>
  </footer>
</body>
</html>
```